I have a logo and need to design the business card and stationery.

The uploaded logo image named as FERNHOLT CONSTRUCTION which is to be replaced to FERNHOLT CONTRACTS. Kindly add below details and submit the designs- Company name- Fernholt Engineering Contracts LLP Name & Post- Varun Kelkar (Designated Partner) Address- Block No.712, Wing C, Tulsa Trade Court, Moti Lal Road, Pawar Industrial Estate, Goregaon(E), Mumbai - 400 063 Contact- +91 97410 58263 Email- varunkelkar@mailnest.example Website- www.fernholtcontracts.example Contact for Letterhead- +91-22-27481195

Hi Tanvir Haque, We are liking your Design #41927306. We have suggested some changes which are mentioned in feedback. Kindly revert with it asap to finalize this design.

Colors

Designer to choose colors to be used in the design.

```html
<!DOCTYPE html>
<html lang="en">
<head>
<meta charset="utf-8">
<title>Fernholt Contracts – Letterhead</title>
<link href="https://fonts.googleapis.com/css2?family=Open+Sans:wght@400;600;700&display=swap" rel="stylesheet">
<style>
  :root {
    --charcoal: #2e2e30;
    --paper: #f4f4f4;
    --backdrop: #dcdcdc;
    --body-text: #5a5a5a;
    --footer-text: #2a2a2a;
    --band-text: #ffffff;
  }
  * { box-sizing: border-box; margin: 0; padding: 0; }
  html, body {
    width: 1200px; height: 884px; overflow: hidden;
    background: var(--backdrop);
    font-family: "Open Sans", Arial, sans-serif;
  }
  .letterhead {
    position: absolute; left: 305px; top: 38px;
    width: 590px; height: 808px;
    background: var(--paper);
    box-shadow: 0 6px 18px rgba(0,0,0,.18);
    display: flex; flex-direction: column;
  }
  .letterhead__header {
    height: 118px; background: var(--charcoal);
    display: flex; justify-content: space-between; align-items: flex-start;
    padding: 30px 40px 0 60px; color: var(--band-text);
  }
  .brand { display: flex; align-items: center; gap: 10px; }
  .brand__mark { width: 22px; height: 22px; border: 2px solid var(--band-text); }
  .brand__name { font-size: 15px; font-weight: 600; letter-spacing: 1.5px; }
  .contact-list {
    list-style: none; align-self: flex-end; padding-bottom: 14px;
    font-size: 10.5px; line-height: 1.55;
  }
  .contact-list li { display: flex; align-items: center; gap: 6px; }
  .contact-list svg { width: 10px; height: 10px; fill: var(--band-text); flex: none; }
  .letter {
    flex: 1; padding: 52px 60px 0 60px;
    color: var(--body-text); font-size: 11.8px; line-height: 1.5;
  }
  .letter__greeting { margin-bottom: 12px; }
  .letter__body p { margin-bottom: 12px; }
  .letter__closing { margin-top: 8px; }
  .signature {
    width: 96px; height: 58px; margin: 14px 0 0 -6px;
    background: linear-gradient(135deg, #e8e8e8, #d6d6d6);
    border-radius: 4px;
  }
  .sender-address {
    padding: 0 60px 26px; color: var(--footer-text);
    font-size: 10.5px; font-weight: 600; line-height: 1.45;
  }
  .letterhead__footer { height: 12px; background: var(--charcoal); }
</style>
</head>
<body>
  <article class="letterhead">
    <header class="letterhead__header">
      <div class="brand">
        <span class="brand__mark"></span>
        <span class="brand__name">FERNHOLT CONTRACTS</span>
      </div>
      <ul class="contact-list">
        <li><svg viewBox="0 0 10 10"><path d="M2 0.5 L3.6 2.6 L2.8 3.6 Q4 6 6.4 7.2 L7.4 6.4 L9.5 8 L8.6 9.5 Q2 8.5 0.5 1.4 Z"/></svg>+91-22-27481195</li>
        <li><svg viewBox="0 0 10 10"><path d="M0.5 2 H9.5 V8.2 H0.5 Z M1 2.4 L5 5.6 L9 2.4" fill="none" stroke="#fff" stroke-width="1"/></svg>info@fernholtcontracts.example</li>
        <li><svg viewBox="0 0 10 10"><circle cx="5" cy="5" r="4.3" fill="none" stroke="#fff" stroke-width="1"/><path d="M0.7 5 H9.3 M5 0.7 Q2.4 5 5 9.3 M5 0.7 Q7.6 5 5 9.3" fill="none" stroke="#fff" stroke-width="0.8"/></svg>www.fernholtcontracts.example</li>
      </ul>
    </header>

    <section class="letter">
      <p class="letter__greeting">Dear customer,</p>
      <div class="letter__body">
        <p>Lorem ipsum dolor sit amet, consectetur adipisicing elit, sed do eiusmod tempor incididunt ut labore et dolore magna aliqua. Ut enim ad minim veniam, quis nostrud exercitation ullamco laboris nisi ut aliquip ex ea commodo consequat. Duis aute irure dolor in reprehenderit in voluptate velit esse cillum dolore eu fugiat nulla pariatur. Excepteur sint occaecat cupidatat non proident, sunt in culpa qui officia deserunt mollit anim id est laborum.</p>
        <p>Lorem ipsum dolor sit amet, consectetur adipisicing elit, sed do eiusmod tempor incididunt ut labore et dolore magna aliqua. Ut enim ad minim veniam, quis nostrud exercitation ullamco laboris nisi ut aliquip ex ea commodo consequat. Duis aute irure dolor in reprehenderit in voluptate velit esse cillum dolore eu fugiat nulla pariatur. Excepteur sint occaecat cupidatat non proident, sunt in culpa qui officia deserunt mollit anim id est laborum.</p>
        <p>Lorem ipsum dolor sit amet, consectetur adipisicing elit, sed do eiusmod tempor incididunt ut labore et dolore magna aliqua. Ut enim ad minim veniam, quis nostrud exercitation ullamco laboris nisi ut aliquip ex ea commodo consequat. Duis aute irure dolor in reprehenderit in voluptate velit esse cillum dolore eu fugiat nulla pariatur. Excepteur sint occaecat cupidatat non proident, sunt in culpa qui officia deserunt mollit anim id est laborum.</p>
        <p>Lorem ipsum dolor sit amet, consectetur adipisicing elit, sed do eiusmod tempor incididunt ut labore et dolore magna aliqua. Ut enim ad minim veniam, quis nostrud exercitation ullamco laboris nisi ut aliquip ex ea commodo consequat. Duis aute irure dolor in reprehenderit.</p>
      </div>
      <p class="letter__closing">Yours Sincerely,</p>
      <div class="signature" role="img" aria-label="Handwritten signature of the sender"></div>
    </section>

    <address class="sender-address" style="font-style: normal;">
      Fernholt Engineering Contracts LLP<br>
      Block No.712, Wing C, Tulsa Trade Court, Moti Lal Road,<br>
      Pawar Industrial Estate, Goregaon(E), Mumbai - 400 063
    </address>
    <footer class="letterhead__footer"></footer>
  </article>
</body>
</html>
```